Vorrel Letterhead

Need a fresh looking design. We are a IT service company and I would like some elements of the logo to flow through. I have included the logo as an attachment. I have also included business card design as it might help with the design.

Industry/Entity Type

Business

```html
<!DOCTYPE html>
<html lang="en">
<head>
<meta charset="utf-8">
<title>Vorrel Letterhead</title>
<link href="https://fonts.googleapis.com/css2?family=Questrial&display=swap" rel="stylesheet">
<style>
  :root {
    --lime: #a5cd4c;
    --slate: #848d93;
    --slate-dark: #6f777c;
    --paper: #ffffff;
    --backdrop: #3d3b39;
    --ink-light: #ffffff;
  }
  * { margin: 0; padding: 0; box-sizing: border-box; }
  html, body { width: 1200px; height: 1000px; overflow: hidden; }
  body {
    background: var(--backdrop);
    font-family: "Questrial", "Century Gothic", sans-serif;
    position: relative;
  }
  .letterhead {
    position: absolute;
    left: 280px;
    top: 47px;
    width: 640px;
    height: 905px;
    background: var(--paper);
    overflow: hidden;
  }
  .letterhead-header {
    position: absolute;
    left: 0; top: 0;
    width: 640px; height: 130px;
  }
  .header-art { position: absolute; left: 0; top: 0; }
  .brand-name {
    position: absolute;
    left: 30px; top: 26px;
    display: flex; align-items: center; gap: 8px;
    color: var(--ink-light);
    font-size: 48px;
    line-height: 1;
    letter-spacing: -0.5px;
  }
  .brand-mark {
    width: 16px; height: 16px;
    background: var(--ink-light);
  }
  .sender {
    position: absolute;
    left: 370px; top: 24px;
    color: var(--ink-light);
    font-size: 7.5px;
    line-height: 1.3;
  }
  .sender-name { font-size: 9px; letter-spacing: 0.3px; }
  .sender-role { color: var(--lime); margin-bottom: 4px; }
  .contact-list { list-style: none; }
  .contact-list li {
    display: flex; align-items: center; gap: 6px;
    height: 10.5px;
  }
  .contact-icon {
    width: 7px; height: 7px;
    border-radius: 50%;
    background: var(--lime);
    flex: none;
  }
  .divider {
    position: absolute;
    left: 475px; top: 37px;
    width: 1px; height: 38px;
    background: var(--ink-light);
  }
  .office {
    position: absolute;
    left: 485px; top: 37px;
    color: var(--ink-light);
    font-size: 7.5px;
  }
  .letterhead-footer {
    position: absolute;
    left: 0; bottom: 0;
    width: 100%; height: 36px;
    background: var(--slate);
  }
</style>
</head>
<body>
  <main class="letterhead">
    <header class="letterhead-header">
      <svg class="header-art" width="640" height="130" viewBox="0 0 640 130" aria-hidden="true">
        <rect x="0" y="0" width="640" height="30" fill="var(--lime)"/>
        <path d="M0 26 Q320 6 640 16 L640 88 L0 88 Z" fill="var(--slate)"/>
        <rect x="0" y="86" width="640" height="5" fill="var(--lime)"/>
        <path d="M0 0 H222 C214 64 160 124 84 124 C44 124 14 110 0 96 Z" fill="var(--slate-dark)"/>
        <path d="M0 0 H214 C206 60 154 119 82 119 C44 119 14 106 0 92 Z" fill="var(--lime)"/>
      </svg>
      <div class="brand-name"><span>Vorrel</span><span class="brand-mark"></span></div>

      <div class="sender">
        <div class="sender-name">MARA KESTEN</div>
        <div class="sender-role">I.T. Consultant</div>
        <ul class="contact-list">
          <li><span class="contact-icon"></span>0400 317 482</li>
          <li><span class="contact-icon"></span>mara@vorrel.com.au</li>
        </ul>
      </div>
      <div class="divider"></div>
      <ul class="office contact-list">
        <li><span class="contact-icon"></span>PO Box 2210, Larkfield 2031</li>
        <li><span class="contact-icon"></span>02 9046 2281</li>
        <li><span class="contact-icon"></span>02 9046 7735</li>
        <li><span class="contact-icon"></span>www.vorrel.com.au</li>
      </ul>
    </header>
    <footer class="letterhead-footer"></footer>
  </main>
</body>
</html>
```